Brightline Energy Product Distribution Brochure

We are looking to have our current brochure for our customers completely redesigned...the idea is to present the relevant information in an attractive way . Our website is brightlineenergyco.example where you can find more information about us. We have included a file with a rough idea of the page order and what each should include but feel free to adapt based on design. The example provided is only for context and doesnt have to be maintained. We will be using the brochure both digitally and in print form. As long as it reads easily and is eye catching, the design can be horizontal or vertical.Final deliverable should be indesign file.

"Our Brands" page: should be limited to one page (space being enough) where it has the header for each one (for example diesel generators) space for one or two lines of text and then the corresponding logos for each of the five categories
Updates

For those asking: the "our brands" page should be a single page layout where there is a header with the corresponding section and space for maybe one line of text followed by the two logos for that category. Each of the product pages should be similar in fashion to the one in the document attached: a photo of the product with some white space and space for the text to be included. We will be posting additional examples today

Target Market(s)

We want to present it to customers both digitally and in print so they can see our products

Industry/Entity Type

Power Generation

Font styles to use
Serif

Requirements
Must have
• Eye catching and able to present the information in a presentable fashion. Rest is up to you.
Nice to have
• Should incorporate the colors of our logo but can also add other depending on design

```html
<!DOCTYPE html>
<html lang="en">
<head>
<meta charset="utf-8">
<title>Brightline Energy — Distributor Program Guide</title>
<link href="https://fonts.googleapis.com/css2?family=Michroma&family=Montserrat:wght@400;600&display=swap" rel="stylesheet">
<style>
  :root {
    --bg: #9c9c9c;
    --paper: #f4f4f4;
    --ink: #4a4a4a;
    --ink-soft: #8a8a8a;
    --band: #505050;
    --brand-yellow: #f2d21b;
    --title-yellow: #f0c419;
    --photo-light: #d9d9d9;
    --photo-mid: #a6a6a6;
    --photo-dark: #5e5e5e;
  }
  * { margin: 0; padding: 0; box-sizing: border-box; }
  html, body { width: 1200px; height: 900px; overflow: hidden; }
  body { background: var(--bg); font-family: "Montserrat", sans-serif; position: relative; }

  .spread {
    position: absolute; left: 80px; top: 255px;
    width: 1040px; height: 390px; display: flex;
    box-shadow: 0 10px 30px rgba(0,0,0,.25);
  }
  .page { position: relative; width: 520px; height: 390px; overflow: hidden; }

  /* Back cover */
  .back-cover { background: var(--paper); }
  .back-cover .edge-art { position: absolute; inset: 0; }
  .back-contact {
    position: absolute; left: 200px; top: 205px; width: 120px;
    text-align: center; color: var(--ink);
  }
  .brand-lockup { display: flex; align-items: center; justify-content: center; gap: 5px; margin-bottom: 8px; }
  .brand-mark { width: 10px; height: 10px; background: var(--brand-yellow); }
  .brand-name { font-size: 8px; font-weight: 600; color: var(--ink); letter-spacing: .5px; text-transform: uppercase; }
  .contact-label { font-size: 4.5px; color: var(--title-yellow); font-weight: 600; margin-top: 3px; }
  .contact-line { font-size: 4.5px; line-height: 1.5; color: var(--ink-soft); }
  .contact-web { font-size: 5px; color: var(--title-yellow); font-weight: 600; margin-top: 3px; }

  /* Front cover */
  .front-cover .cover-photo {
    position: absolute; inset: 0;
    background: linear-gradient(120deg, var(--photo-light) 0%, var(--photo-mid) 45%, var(--photo-dark) 100%);
  }
  .front-cover .cover-shapes { position: absolute; inset: 0; }
  .cover-brand {
    position: absolute; left: 335px; top: 98px;
    display: flex; align-items: center; gap: 6px;
  }
  .cover-brand .brand-mark { width: 13px; height: 13px; }
  .cover-brand .brand-name { font-size: 9px; }
  .cover-title {
    position: absolute; left: 120px; top: 238px;
    font-family: "Michroma", sans-serif; font-size: 21px; line-height: 1.02;
    color: #ffffff; letter-spacing: 1px;
  }
  .cover-title .accent { color: var(--title-yellow); font-weight: 700; }
</style>
</head>
<body>
  <main class="spread">
    <section class="page back-cover">
      <svg class="edge-art" width="520" height="390" viewBox="0 0 520 390">
        <defs>
          <linearGradient id="stripTone" x1="0" y1="0" x2="1" y2="1">
            <stop offset="0" stop-color="#cfcfcf"/>
            <stop offset="1" stop-color="#7a7a7a"/>
          </linearGradient>
        </defs>
        <polygon points="350,0 400,0 520,200 520,300" fill="var(--band)"/>
        <polygon points="400,0 520,0 520,200" fill="url(#stripTone)" role="img" aria-label="Close-up photograph of generator engine parts"/>
      </svg>
      <div class="back-contact">
        <div class="brand-lockup"><span class="brand-mark"></span><span class="brand-name">Brightline Energy</span></div>
        <div class="contact-label">Toll Free: 1-800-555-0142</div>
        <div class="contact-label">Local</div>
        <div class="contact-line">305-555-0187</div>
        <div class="contact-label">Office</div>
        <div class="contact-line">Brightline Energy Inc.</div>
        <div class="contact-line">1200 Harbor Way,</div>
        <div class="contact-line">Springfield, ST 00000, USA</div>
        <div class="contact-web">brightlineenergyco.example</div>
      </div>
    </section>

    <section class="page front-cover">
      <div class="cover-photo" role="img" aria-label="Black and white photograph of a diesel generator engine with turbocharger and piping"></div>
      <svg class="cover-shapes" width="520" height="390" viewBox="0 0 520 390">
        <polygon points="0,0 90,0 0,160" fill="#ffffff" opacity=".25"/>
        <polygon points="150,0 260,0 90,390 0,390 0,340" fill="#ffffff" opacity=".18"/>
        <polygon points="400,0 520,0 520,390 330,390" fill="#2a2a2a" opacity=".15"/>
        <polygon points="400,5 505,110 400,215 295,110" fill="#ffffff" opacity=".9"/>
        <polygon points="470,0 520,0 520,90" fill="var(--brand-yellow)" opacity=".9"/>
        <polygon points="520,120 520,260 420,230" fill="var(--brand-yellow)" opacity=".55"/>
      </svg>
      <div class="cover-brand"><span class="brand-mark"></span><span class="brand-name">Brightline Energy</span></div>
      <h1 class="cover-title">DISTRIBUTOR<br>PROGRAM<br><span class="accent">GUIDE</span></h1>
    </section>
  </main>
</body>
</html>
```